Newsletter-Design für Veroth
Zielgruppe
Digitalisierung von Cyber Security, Risikomanagement und Compliance, die aktuell endlose Emails und komplizierte Tabellenkalkulationen umgesetzt werden. Wir machen das Management von Unternehmensrisiken digital, modern und so einfach wie ein 'Like auf Social Media'.
Zielgruppe sind Organisationen aller Größen und Industrien, über große Firmen zu Krankenhäusern. Wir entwickeln eine moderne und am Puls der Zeit ansässige Software, was auch in unserem Newsletter Design wieder gespiegelt werden soll.
Gerne möchten wir mit dem ausgewählten Designer weiter zusammenarbeiten, da wir schon seit längerem auf der Suche nach einem passenden Freelancer sind.
Aufgabenstellung
Hier finden Sie eine Übersicht über unsere Corporate Identity, Brandfarben und unser Logo zum Download:
https://company-46538.markenplanix.com/d/QWKSGF9h0irf/veroth-style-guide
Zu verwenden sind natürlich die Primary Colors und unsere verwendeten Schriftarten. Auf https://www.veroth.com/de/ finden sich Beispiele von deren Verwendung. Wir wünschen uns ein modernes und ansprechendes Design für eine weite Bandbreite an Kunden.

```html
<!DOCTYPE html>
<html lang="de">
<head>
<meta charset="utf-8">
<title>Veroth Newsletter – Interaktives Layout</title>
<link href="https://fonts.googleapis.com/css2?family=Open+Sans:wght@300;400;600;700&display=swap" rel="stylesheet">
<style>
  :root{
    --teal:#48b9b3;
    --green:#8cc43f;
    --dark:#3b3a36;
    --ink:#2a2a2a;
    --grey:#6d6d6d;
    --pale-blue:#d4e9ec;
    --line:#d9d9d9;
    --white:#ffffff;
  }
  *{box-sizing:border-box;margin:0;padding:0}
  html,body{width:849px;height:1200px;overflow:hidden;background:var(--white)}
  body{font-family:"Open Sans",Arial,sans-serif;color:var(--ink);position:relative}
  .abs{position:absolute}
  .photo{position:absolute}
  .page{position:absolute;background:var(--white);overflow:hidden;border:1px solid var(--line)}
  .shape{position:absolute;left:0;top:0}
  .brand-tag{position:absolute;display:flex;align-items:center;gap:4px;color:var(--white);letter-spacing:.06em}
  .brand-tag .brand-name{font-weight:600}
  .brand-tag .label{border-bottom:1px solid var(--white);font-weight:400}
  .menu-icon{position:absolute;background:var(--white);border:1px solid #bbb}
  .page-no{position:absolute;font-size:5px;color:var(--dark)}
  .headline{position:absolute;color:var(--white);font-weight:300;line-height:1}
  .subline{position:absolute;color:var(--white);font-weight:400}
  .subline b{font-weight:700}
  .intro{position:absolute;font-weight:700;color:var(--ink)}
  .tiny{font-size:3.6px;line-height:1.35;color:var(--grey)}

  /* hero */
  .hero{left:125px;top:48px;width:600px;height:450px;box-shadow:0 2px 14px rgba(0,0,0,.12)}
  .hero .brand-tag{left:36px;top:26px;font-size:11px}
  .hero .headline{left:34px;top:234px;font-size:34px}
  .hero .subline{left:36px;top:308px;font-size:12px}
  .hero .subline b{font-size:13px}
  .hero .intro{left:205px;top:360px;width:300px;font-size:8.5px;line-height:1.4}

  /* cover */
  .cover{left:21px;top:617px;width:256px;height:160px;border:none}
  .cover-bar{position:absolute;left:0;top:0;width:256px;height:18px;background:var(--dark);color:var(--white);font-size:7px;letter-spacing:.06em}
  .cover-bar .label{position:absolute;left:168px;top:4px;border-bottom:1px solid var(--white)}
  .cover-bar .issue{position:absolute;left:222px;top:4px;font-weight:300}
  .cover-brand{position:absolute;left:12px;top:30px;color:var(--white);font-size:20px;font-weight:400;display:flex;align-items:center;gap:5px}
  .cover-brand i{display:block;width:12px;height:12px;border-radius:50%;background:var(--white)}
  .toc{position:absolute;left:9px;top:71px;width:115px;height:69px;background:rgba(255,255,255,.72);padding:4px 6px 0 14px}
  .toc h3{font-size:5px;font-weight:600;color:var(--dark);margin-bottom:2px}
  .toc li{list-style:none;display:flex;justify-content:space-between;font-size:5px;color:var(--grey);line-height:9.3px;font-weight:400}

  .pitch{position:absolute;left:21px;top:832px;font-size:18px;font-weight:300;line-height:20.5px;color:var(--dark)}
  .pitch ul{list-style:none}
  .pitch li{font-weight:700}
  .pitch li::before{content:"•";display:inline-block;width:26px}

  /* article page */
  .article{left:302px;top:617px;width:257px;height:546px}
  .article .brand-tag,.security .brand-tag{left:10px;top:8px;font-size:5px}
  .article .headline{left:9px;top:117px;font-size:12px;line-height:12px}
  .article .subline{left:9px;top:145px;font-size:5px}
  .article .intro{left:64px;top:174px;width:124px;font-size:3.6px;line-height:1.4}
  .step-num{position:absolute;width:17px;height:17px;border:1px solid var(--teal);color:var(--teal);font-size:13px;font-weight:300;text-align:center;line-height:16px}
  .step-note{position:absolute;left:14px;width:58px;text-align:right}
  .step-note.strong{font-weight:700;color:var(--ink)}
  .detail-box{position:absolute;left:84px;top:205px;width:112px;height:115px;border:1px solid var(--teal);padding:3px 4px;overflow:hidden}
  .detail-box p{font-size:4.2px;line-height:1.45;color:var(--grey)}
  .divider{position:absolute;left:103px;top:350px;width:71px;border-top:1px solid var(--dark)}
  .section-title{position:absolute;left:0;top:369px;width:257px;text-align:center;font-size:13px;font-weight:300;color:var(--dark)}
  .faq-slider{position:absolute;left:32px;top:396px;width:191px;height:54px;background:var(--pale-blue)}
  .mail{display:flex;align-items:center;gap:2px;font-size:3.6px;color:var(--teal);font-weight:600}
  .contact{position:absolute;left:64px;top:484px;width:72px}
  .pager{position:absolute;font-size:5px;color:var(--dark);letter-spacing:1px}
  .tools{position:absolute;display:flex;flex-direction:column;gap:3px}
  .tools span{display:block;width:6px;height:6px;border:1px solid #888;background:#f1f1f1}

  /* security page */
  .security{left:572px;top:617px;width:256px;height:398px}
  .security .headline{left:162px;top:30px;font-size:12px}
  .security .subline{left:162px;top:46px;font-size:5px}
  .security .intro{left:42px;top:175px;width:148px;font-size:4px;line-height:1.4}
  .security .body{position:absolute;left:64px;top:207px;width:104px}
  .security .body p{font-size:3.6px;line-height:1.5;color:var(--grey);margin-bottom:4px}
  .aside{position:absolute;border-top:1px solid var(--dark);border-bottom:1px solid var(--dark);padding:2px 0}
  .aside .kicker{font-size:5px;color:var(--green);display:block}
  .aside strong{font-size:5.6px;line-height:1.2;color:var(--ink);font-weight:700;display:block}
  .search-btn{position:absolute;left:64px;top:373px;width:90px;height:12px;background:var(--green);color:var(--white);font-size:3.6px;font-weight:700;display:flex;align-items:center;gap:3px;padding-left:3px;line-height:1.2}
</style>
</head>
<body>

<!-- Title screen -->
<section class="page hero">
  <div class="photo" role="img" aria-label="Photo of a manager at his desk reading documents" style="left:0;top:0;width:600px;height:330px;background:linear-gradient(120deg,#c9cdc6 0%,#a9ada0 35%,#e6e4df 60%,#8d9189 100%)"></div>
  <svg class="shape" width="600" height="330" viewBox="0 0 600 330"><polygon points="0,62 0,330 330,330" fill="#48b9b3"/></svg>
  <div class="brand-tag"><span class="brand-name">veroth</span><span class="label">NEWSLETTER</span></div>
  <div class="menu-icon" style="left:16px;top:118px;width:16px;height:16px"></div>
  <div class="page-no" style="left:574px;top:16px;font-size:9px">3</div>
  <svg class="abs" style="left:38px;top:170px" width="20" height="38"><polyline points="17,2 3,19 17,36" fill="none" stroke="#8cc43f" stroke-width="3"/></svg>
  <svg class="abs" style="left:548px;top:114px" width="20" height="38"><polyline points="3,2 17,19 3,36" fill="none" stroke="#8cc43f" stroke-width="3"/></svg>
  <h1 class="headline">Ask the<br>management</h1>
  <p class="subline"><b>Max Muster</b> answers your questions</p>
  <p class="intro">Quatene aturia plit quas volorest, utaspidunt, qui vent, quaturibus, con con cum se sim exceperibus min pellorporrum disi consequis moluptatusae peratur? Obitaqu iduntin cimporescia cumquatus, voloria sum eos repeliqui doluptas.</p>
</section>

<!-- Cover page -->
<section class="page cover">
  <div class="photo" role="img" aria-label="Photo of two colleagues working at a computer" style="left:0;top:18px;width:256px;height:142px;background:linear-gradient(110deg,#5f6b76 0%,#c9b7a1 45%,#7c8894 75%,#3e4b58 100%)"></div>
  <svg class="shape" width="256" height="160" viewBox="0 0 256 160"><polygon points="0,18 183,18 34,160 0,160" fill="#8cc43f"/></svg>
  <div class="cover-bar"><span class="label">NEWSLETTER</span><span class="issue">2|2017</span></div>
  <div class="cover-brand"><i></i>veroth</div>
  <div class="menu-icon" style="left:1px;top:71px;width:7px;height:7px"></div>
  <nav class="toc">
    <h3>Table of contents in this issue</h3>
    <ul>
      <li><span>Greetings</span><span>2</span></li>
      <li><span>Questions to the management</span><span>3</span></li>
      <li><span>Topic of the month</span><span>4</span></li>
      <li><span>Inside veroth</span><span>5 - 6</span></li>
      <li><span>News from the market</span><span>7 - 8</span></li>
      <li><span>A day with ...</span><span>9</span></li>
    </ul>
  </nav>
</section>

<div class="pitch">
  Interaktiv gestaltet mit
  <ul><li>Hyperlinks</li><li>Wipe-Buttons</li></ul>
  zum einfachen navigieren<br>innerhalb des Newsletters.
</div>

<!-- Article page -->
<section class="page article">
  <div class="photo" role="img" aria-label="Photo of a manager at his desk reading documents" style="left:0;top:0;width:257px;height:160px;background:linear-gradient(120deg,#c9cdc6 0%,#a9ada0 35%,#e6e4df 60%,#8d9189 100%)"></div>
  <svg class="shape" width="257" height="160" viewBox="0 0 257 160"><polygon points="0,38 0,160 115,160" fill="#48b9b3"/></svg>
  <div class="brand-tag"><span class="brand-name">veroth</span><span class="label">NEWSLETTER</span></div>
  <div class="menu-icon" style="left:1px;top:37px;width:7px;height:7px"></div>
  <div class="page-no" style="left:243px;top:9px">3</div>
  <svg class="abs" style="left:9px;top:79px" width="9" height="16"><polyline points="8,1 1,8 8,15" fill="none" stroke="#8cc43f" stroke-width="1.3"/></svg>
  <svg class="abs" style="left:236px;top:79px" width="9" height="16"><polyline points="1,1 8,8 1,15" fill="none" stroke="#8cc43f" stroke-width="1.3"/></svg>
  <h2 class="headline">Ask the<br>management</h2>
  <p class="subline"><b>Max Muster</b> answers your questions</p>
  <p class="intro">Quatene aturia plit quas volorest, utaspidunt, qui vent, quaturibus, con con cum se sim exceperibus min pellorporrum disi consequis moluptatusae peratur? Obitaqu iduntin cimporescia cumquatus, voloria sum eos repeliqui doluptas.</p>

  <div class="step-num" style="left:55px;top:205px">1</div>
  <svg class="abs" style="left:69px;top:201px" width="7" height="7"><rect x=".5" y=".5" width="6" height="6" fill="#8cc43f"/><path d="M3.5 2v3M2 3.5h3" stroke="#fff" stroke-width=".8"/></svg>
  <p class="step-note tiny" style="top:225px">Short notes on the first question and how our team answers it today.</p>

  <div class="step-num" style="left:55px;top:256px">2</div>
  <svg class="abs" style="left:69px;top:252px" width="7" height="7"><rect x=".5" y=".5" width="6" height="6" fill="#48b9b3"/><path d="M2 3.5h3" stroke="#fff" stroke-width=".8"/></svg>
  <p class="step-note tiny strong" style="top:277px">Key facts on risk reviews and how audits run in every unit.</p>

  <div class="step-num" style="left:55px;top:302px">3</div>
  <svg class="abs" style="left:69px;top:298px" width="7" height="7"><rect x=".5" y=".5" width="6" height="6" fill="#8cc43f"/><path d="M3.5 2v3M2 3.5h3" stroke="#fff" stroke-width=".8"/></svg>
  <p class="step-note tiny" style="top:322px">Our tools make compliance tasks simple, quick and clear for every team member at work.</p>

  <div class="detail-box"><p>Risk work should not live in long email threads or complex sheets. With one shared view, every team sees open tasks, due dates and owners. Reviews move faster, audits stay clear and managers can act early. This issue explains how we plan the next steps and which features arrive in spring for all users. We also look at feedback from hospitals, banks and mid-sized firms who moved their controls online last year. Their teams report fewer meetings, shorter audit cycles and a far better overview of open findings. Read on to learn which changes they made first and what helped staff adopt the new tools within weeks.</p></div>

  <div class="divider"></div>
  <h3 class="section-title">Borepudam ad eatem aut</h3>

  <div class="faq-slider">
    <svg class="abs" style="left:12px;top:18px" width="9" height="18"><polyline points="8,1 1,9 8,17" fill="none" stroke="#fff" stroke-width="1.3"/></svg>
    <svg class="abs" style="left:171px;top:18px" width="9" height="18"><polyline points="1,1 8,9 1,17" fill="none" stroke="#fff" stroke-width="1.3"/></svg>
    <svg class="abs" style="left:33px;top:10px" width="62" height="18" viewBox="0 0 62 18">
      <path d="M1 1h11v10H6l-3 3v-3H1z" fill="#fff" stroke="#555" stroke-width=".6"/>
      <text x="4.2" y="8.8" font-size="8" fill="#555" font-family="Open Sans, sans-serif">?</text>
      <path d="M15 6h22v-2l4 3-4 3v-2H15z" fill="#fff" stroke="#555" stroke-width=".6"/>
      <rect x="49" y="1" width="10" height="11" fill="#555"/>
      <rect x="53.4" y="3" width="1.4" height="5" fill="#fff"/><rect x="53.4" y="9" width="1.4" height="1.4" fill="#fff"/>
    </svg>
    <p class="tiny" style="position:absolute;left:96px;top:3px;width:64px;color:#444">Send us your question and our team will reply within two working days by email.</p>
    <div class="mail" style="position:absolute;left:96px;top:36px">
      <svg width="5" height="4"><rect x=".3" y=".3" width="4.4" height="3.4" fill="none" stroke="#48b9b3" stroke-width=".5"/><polyline points=".3,.3 2.5,2 4.7,.3" fill="none" stroke="#48b9b3" stroke-width=".5"/></svg>support@veroth.com</div>
    <svg class="abs" style="left:90px;top:48px" width="12" height="3"><circle cx="1.5" cy="1.5" r="1.2" fill="#fff"/><circle cx="5.5" cy="1.5" r="1" fill="none" stroke="#fff" stroke-width=".5"/><circle cx="9.5" cy="1.5" r="1" fill="none" stroke="#fff" stroke-width=".5"/></svg>
  </div>

  <div class="contact">
    <p class="tiny" style="color:#444">Write to us any time with ideas, questions or topics for the next issue.</p>
    <div class="mail" style="margin-top:6px">
      <svg width="5" height="4"><rect x=".3" y=".3" width="4.4" height="3.4" fill="none" stroke="#48b9b3" stroke-width=".5"/><polyline points=".3,.3 2.5,2 4.7,.3" fill="none" stroke="#48b9b3" stroke-width=".5"/></svg>support@veroth.com</div>
  </div>
  <div class="photo" role="img" aria-label="Portrait photo of a support team member" style="left:147px;top:469px;width:46px;height:46px;background:linear-gradient(160deg,#2e9fd6,#1b6fa8)"></div>

  <div class="tools" style="left:248px;top:510px"><span></span><span></span><span></span></div>
  <div class="pager" style="left:222px;top:530px">«‹ ›»</div>
</section>

<!-- Security page -->
<section class="page security">
  <div class="photo" role="img" aria-label="Photo of a security guard holding a radio" style="left:0;top:0;width:256px;height:160px;background:linear-gradient(110deg,#4a4f52 0%,#8d9a8f 45%,#c7cfc6 75%,#9aa597 100%)"></div>
  <svg class="shape" width="256" height="160" viewBox="0 0 256 160"><polygon points="66,0 256,0 256,138" fill="#8cc43f"/></svg>
  <div class="brand-tag"><span class="brand-name">veroth</span><span class="label">NEWSLETTER</span></div>
  <div class="menu-icon" style="left:1px;top:37px;width:7px;height:7px"></div>
  <div class="page-no" style="left:243px;top:9px;color:#fff">4</div>
  <svg class="abs" style="left:9px;top:79px" width="9" height="16"><polyline points="8,1 1,8 8,15" fill="none" stroke="#48b9b3" stroke-width="1.3"/></svg>
  <svg class="abs" style="left:236px;top:79px" width="9" height="16"><polyline points="1,1 8,8 1,15" fill="none" stroke="#48b9b3" stroke-width="1.3"/></svg>
  <h2 class="headline">Security 4.0</h2>
  <p class="subline">Exeri alitam sit Equi dis sandi ut.</p>
  <p class="intro">Et est faccae porepella doluptam il molorum fugit eos et ad qui aut vent pere velestrum, eos estibus ellorem voluptatusam eosape es cum reiusti asperio tendem et el et impera cus atempor magni opta nonse nobis sa verferi animint enderfe rendaeces et eum ne</p>

  <div class="body">
    <p>Security teams need a clear view of every risk. Our new module links controls, tasks and owners in one place, so nothing gets lost between departments or slips through during handovers.</p>
    <p>Each check shows its status at a glance. Reports are ready in seconds and can be shared with auditors or the board without extra work. Owners get a short reminder when a control is due, and managers see at once where support is needed.</p>
    <p>Plans for the next release include smarter alerts, simple mobile access and templates for common standards, so new teams can start on day one.</p>
    <p>We thank all customers who joined our pilot and shared their ideas with us. Your feedback shapes every step of our roadmap.</p>
  </div>

  <aside class="aside" style="left:198px;top:217px;width:52px"><span class="kicker">Lorem</span><strong>Harit que rectaquas eius magnimped moditam re mo modi consequis sinihicid quae</strong></aside>
  <aside class="aside" style="left:25px;top:293px;width:34px"><span class="kicker">Lorem</span><strong>Volecepudae voluptas eaqui vent aribus dolorpo</strong></aside>

  <div class="photo" role="img" aria-label="Portrait photo of a smiling team lead" style="left:171px;top:309px;width:39px;height:47px;background:linear-gradient(160deg,#d9dcd2,#a7ab9d)"></div>
  <p class="tiny" style="position:absolute;left:171px;top:358px;width:39px;font-size:2.6px;border-bottom:1px solid #333">Team lead, security office</p>

  <div class="search-btn">
    <svg width="8" height="8"><circle cx="3.5" cy="3.5" r="2.6" fill="none" stroke="#fff" stroke-width=".8"/><line x1="5.4" y1="5.4" x2="7.6" y2="7.6" stroke="#fff" stroke-width=".8"/></svg>
    <span>Find more articles on security<br>in our archive</span>
  </div>

  <div class="tools" style="left:248px;top:355px"><span></span><span></span><span></span></div>
  <div class="pager" style="left:222px;top:375px">«‹ ›»</div>
</section>

</body>
</html>
```